Rising Harbor Glow Gala Graphic Design

I’m seeking a professional graphic designer experienced in event branding to create a cohesive suite of materials for our third annual fundraising gala, “Rising Harbor Glow.” This year's theme is " An Evening in Silver for Rising Harbor Glow" Need to design collateral for website, social media and email blasts.
Target Market(s)
Affluent gala attendees
Industry/Entity Type
Fundraising / Charity / Outdoors / Sports
Font styles to use
Decorative
Script
Colors
0054AA
0677BA
7BADD7
CADEEF
E8F1F8
0094D4
00A9DD
6FCCEA
C7EBF8
E9F6FB
00AB8E
00BBA5
67D7C9
C6EFE9
E9F9F6
6B429C
8869AF
B7A5CE
E3DAEB
F3F0F8

```html
<!DOCTYPE html>
<html lang="en">
<head>
<meta charset="utf-8">
<title>Rising Harbor Glow – Gala Collateral</title>
<link href="https://fonts.googleapis.com/css2?family=Cinzel:wght@400;600;700&family=Marcellus&family=Great+Vibes&display=swap" rel="stylesheet">
<style>
:root{
  --board:#d6d6d6;
  --sea-deep:#00877a;
  --sea-mid:#00ab8e;
  --sea-light:#00bba5;
  --sea-shade:rgba(0,84,90,.45);
  --sea-glint:rgba(233,249,246,.3);
  --blue:#0054aa;
  --blue-mid:#0677ba;
  --teal:#00ab8e;
  --navy:#0b2f5a;
  --grey:#6b7480;
  --silver-1:#76828f;
  --silver-2:#d9e0e7;
  --silver-3:#8c98a5;
  --silver-line:#a6b1bc;
  --mist-1:#e9f6fb;
  --mist-2:#c7ebf8;
  --panel:#0054aa;
  --star:#cadeef;
  --white:#ffffff;
}
*{margin:0;padding:0;box-sizing:border-box}
html,body{width:800px;height:1200px;overflow:hidden;background:var(--board)}
.board{position:relative;width:800px;height:1200px}
.flyer{position:absolute;background:var(--white);overflow:hidden;text-align:center;box-shadow:0 1px 3px rgba(0,0,0,.12)}
.flyer--invite{left:219px;top:61px;width:371px;height:522px}
.flyer--together{left:100px;top:642px;width:268px;height:477px}
.flyer--vip{left:432px;top:642px;width:268px;height:477px}
.block{position:absolute;left:0;right:0}
.sea{position:absolute;left:0;right:0;
  background:
   radial-gradient(ellipse 30% 22% at 75% 30%,var(--sea-shade),transparent 70%),
   radial-gradient(ellipse 25% 18% at 88% 70%,var(--sea-shade),transparent 70%),
   radial-gradient(ellipse 22% 30% at 22% 45%,var(--sea-glint),transparent 70%),
   linear-gradient(160deg,var(--sea-light),var(--sea-mid) 45%,var(--sea-deep));}
.sea--foot{background:
   radial-gradient(ellipse 20% 40% at 70% 50%,var(--sea-shade),transparent 70%),
   linear-gradient(160deg,var(--sea-mid),var(--sea-deep));}
.silver-rule{position:absolute;left:0;right:0;height:2px;background:linear-gradient(90deg,var(--silver-1),var(--silver-2),var(--silver-1))}
.org-name{position:absolute;display:flex;align-items:flex-start;gap:5px;text-align:left;color:var(--white);font-family:"Marcellus",serif;line-height:1.02}
.org-name .dot{width:8px;height:8px;border-radius:50%;background:var(--white);margin-top:3px;flex:none}
.org-name small{display:block;font-size:.5em;margin-top:2px}
.lead{position:absolute;left:0;right:0;font-family:"Cinzel",serif;font-weight:600;color:var(--white);line-height:1.15;letter-spacing:.02em}
.title-top{font-family:"Cinzel",serif;color:var(--blue);line-height:1;letter-spacing:.02em}
.title-mid{display:flex;align-items:center;justify-content:center;gap:10px;font-family:"Great Vibes",cursive;color:var(--navy);line-height:1}
.title-mid::before,.title-mid::after{content:"";width:var(--rule-w,46px);height:5px;border-top:1px solid var(--silver-line);border-bottom:1px solid var(--silver-line)}
.silver-text{background:linear-gradient(180deg,var(--silver-2),var(--silver-1) 55%,var(--silver-3));-webkit-background-clip:text;background-clip:text;color:transparent}
.title-bottom{font-family:"Cinzel",serif;line-height:1;letter-spacing:.02em}
.gala{font-family:"Cinzel",serif;font-weight:600;color:var(--navy);letter-spacing:.12em}
.sub{font-family:"Marcellus",serif;color:var(--grey);letter-spacing:.12em;line-height:1.35}
.script{font-family:"Great Vibes",cursive;line-height:1.2}
.details{font-family:"Marcellus",serif;color:var(--grey);letter-spacing:.1em;line-height:1.3}
.details b{font-family:"Cinzel",serif;font-weight:700;color:var(--navy)}
.url{font-family:"Cinzel",serif;font-weight:700;letter-spacing:.02em}
.mist{position:absolute;left:0;right:0;background:linear-gradient(180deg,rgba(233,246,251,0),var(--mist-1) 25%,var(--mist-2) 80%,rgba(233,246,251,.6))}
.cta{position:absolute;left:50%;transform:translateX(-50%);background:linear-gradient(90deg,var(--silver-3),var(--silver-2),var(--silver-3));clip-path:polygon(3% 0,97% 0,100% 100%,0 100%);color:var(--navy);font-family:"Marcellus",serif;letter-spacing:.12em;display:flex;align-items:center;justify-content:center}
.tiny{font-family:"Marcellus",serif;color:var(--grey);font-size:4.6px;letter-spacing:.08em}
.perks{position:absolute;left:20px;right:21px;background:var(--panel);border-radius:0 0 8px 8px;display:grid;grid-template-columns:repeat(4,1fr);padding:6px 4px;gap:6px 2px}
.perk{display:flex;align-items:center;gap:3px;text-align:left;color:var(--white);font-family:"Cinzel",serif;font-size:4.6px;line-height:1.15}
.perk svg{width:8px;height:8px;flex:none}
.perk path{fill:var(--star)}
.vip-line{display:flex;align-items:baseline;justify-content:center;gap:5px}
</style>
</head>
<body>
<div class="board">

  <section class="flyer flyer--invite">
    <div class="sea" style="top:0;height:161px" role="img" aria-label="Aerial photo of an offshore beacon tower on turquoise reef water"></div>
    <div class="org-name" style="left:188px;top:52px;font-size:11.5px"><span class="dot"></span><span>SAVE<br>HARBOR<br>BEACON<small>Coral Point, Gulf Shores</small></span></div>
    <div class="lead" style="top:130px;font-size:11.5px">YOU ARE CORDIALLY<br>INVITED TO</div>
    <div class="silver-rule" style="top:160px"></div>
    <div class="block title-top" style="top:175px;font-size:31px">RISING</div>
    <div class="block title-mid" style="top:205px;font-size:27px;--rule-w:48px">Harbor</div>
    <div class="block title-bottom silver-text" style="top:236px;font-size:42px">GLOW</div>
    <div class="block gala" style="top:288px;font-size:12px">A FUNDRAISING GALA</div>
    <div class="block sub" style="top:304px;font-size:9.6px">IN CELEBRATION OF OUR THIRD ANNUAL GALA<br>FOR HARBOR REEF BEACON</div>
    <div class="block script" style="top:338px;font-size:22px;color:var(--blue-mid)">For her brightest years to come!</div>
    <div class="mist" style="top:370px;height:82px"></div>
    <div class="block details" style="top:381px;font-size:8.8px">
      <b>WHEN:</b>NOVEMBER 18TH, 2025<br>COCKTAILS 6:00PM | VIP TICKET HOLDERS 5:00PM<br>
      <b>WHERE:</b> PELICAN KEY - 4120 SEASIDE HWY<br>CORAL POINT<br>
      <b>DRESS:</b> COCKTAIL ATTIRE - <b>SPACE IS LIMITED</b></div>
    <div class="block url" style="top:462px;font-size:8.5px;color:var(--navy)">WWW.SAVEHARBORBEACON.ORG</div>
    <div class="silver-rule" style="top:482px"></div>
    <div class="sea sea--foot" style="top:484px;height:38px" role="img" aria-label="Turquoise reef water"></div>
  </section>

  <section class="flyer flyer--together">
    <div class="sea" style="top:0;height:137px" role="img" aria-label="Aerial photo of an offshore beacon tower on turquoise reef water"></div>
    <div class="org-name" style="left:140px;top:40px;font-size:9px"><span class="dot" style="width:6px;height:6px"></span><span>SAVE<br>HARBOR<br>BEACON<small>Coral Point, Gulf Shores</small></span></div>
    <div class="lead" style="top:108px;font-size:10.5px">LET'S COME<br>TOGETHER TO</div>
    <div class="silver-rule" style="top:136px"></div>
    <div class="block title-top" style="top:150px;font-size:27px;color:var(--teal)">RISING</div>
    <div class="block title-mid" style="top:176px;font-size:22px;--rule-w:40px">Harbor</div>
    <div class="block title-bottom silver-text" style="top:199px;font-size:35px">GLOW</div>
    <div class="block gala" style="top:241px;font-size:10px">A FUNDRAISING GALA</div>
    <div class="block sub" style="top:256px;font-size:7.4px">IN CELEBRATION OF OUR THIRD ANNUAL GALA<br>FOR HARBOR REEF BEACON</div>
    <div class="block script" style="top:290px;font-size:13px;color:var(--blue-mid)">Join us for a luminous evening of dining, delectable<br>libations, live entertainment, artistry and more!</div>
    <div class="cta" style="top:333px;width:174px;height:21px;font-size:9px">GET YOUR TICKETS TODAY!</div>
    <div class="block tiny" style="top:361px">BE PART OF THE MOVEMENT TO #SAVEHARBORBEACON</div>
    <div class="block details" style="top:381px;font-size:7.3px">
      <b>WHEN:</b>NOVEMBER 18TH, 2025<br>COCKTAILS 6:00PM | VIP TICKET HOLDERS 5:00PM<br>
      <b>WHERE:</b> PELICAN KEY - 4120 SEASIDE HWY<br>CORAL POINT<br>
      <b>DRESS:</b> COCKTAIL ATTIRE - <b>SPACE IS LIMITED</b></div>
    <div class="silver-rule" style="top:438px"></div>
    <div class="sea sea--foot" style="top:440px;height:37px" role="img" aria-label="Turquoise reef water"></div>
    <div class="block url" style="top:453px;font-size:7.6px;color:var(--white)">WWW.SAVEHARBORBEACON.ORG</div>
  </section>

  <section class="flyer flyer--vip">
    <div class="sea" style="top:0;height:111px" role="img" aria-label="Aerial photo of an offshore beacon tower on turquoise reef water"></div>
    <div class="org-name" style="left:136px;top:30px;font-size:8px"><span class="dot" style="width:6px;height:6px"></span><span>SAVE<br>HARBOR<br>BEACON<small>Coral Point, Gulf Shores</small></span></div>
    <div class="lead" style="top:85px;font-size:9.5px">LET'S COME<br>TOGETHER TO</div>
    <div class="silver-rule" style="top:110px"></div>
    <div class="block title-top" style="top:120px;font-size:22px;color:var(--teal)">RISING</div>
    <div class="block title-mid" style="top:142px;font-size:19px;--rule-w:32px">Harbor</div>
    <div class="block title-bottom silver-text" style="top:161px;font-size:30px">GLOW</div>
    <div class="block gala" style="top:199px;font-size:8.6px">A FUNDRAISING GALA</div>
    <div class="block sub" style="top:212px;font-size:6.4px">IN CELEBRATION OF OUR THIRD ANNUAL GALA<br>FOR HARBOR REEF BEACON</div>
    <div class="block script" style="top:238px;font-size:10px;color:var(--navy)">Light up the night with an exclusive</div>
    <div class="block vip-line" style="top:249px"><span class="title-bottom silver-text" style="font-size:26px">VIP</span><span class="title-top" style="font-size:15px;font-weight:600;color:var(--navy)">PACKAGE</span></div>
    <div class="block script" style="top:277px;font-size:9.5px;color:var(--navy);line-height:1.05">your silver ticket to a remarkable<br>night of glamour and philanthropy.</div>
    <div class="cta" style="top:311px;width:128px;height:14px;font-size:6.4px">GET YOUR TICKETS TODAY!</div>
    <div class="perks" style="top:325px">
      <div class="perk"><svg viewBox="0 0 10 10"><path d="M5 0l1.5 3.3 3.5.4-2.6 2.4.7 3.5L5 7.8 1.9 9.6l.7-3.5L0 3.7l3.5-.4z"/></svg>VIP PRE GALA EXPERIENCE</div>
      <div class="perk"><svg viewBox="0 0 10 10"><path d="M5 0l1.5 3.3 3.5.4-2.6 2.4.7 3.5L5 7.8 1.9 9.6l.7-3.5L0 3.7l3.5-.4z"/></svg>DELICIOUS DINNER FOR 10</div>
      <div class="perk"><svg viewBox="0 0 10 10"><path d="M5 0l1.5 3.3 3.5.4-2.6 2.4.7 3.5L5 7.8 1.9 9.6l.7-3.5L0 3.7l3.5-.4z"/></svg>UNLIMITED PREMIUM BAR</div>
      <div class="perk"><svg viewBox="0 0 10 10"><path d="M5 0l1.5 3.3 3.5.4-2.6 2.4.7 3.5L5 7.8 1.9 9.6l.7-3.5L0 3.7l3.5-.4z"/></svg>EXCLUSIVE MEET &amp; GREET</div>
      <div class="perk"><svg viewBox="0 0 10 10"><path d="M5 0l1.5 3.3 3.5.4-2.6 2.4.7 3.5L5 7.8 1.9 9.6l.7-3.5L0 3.7l3.5-.4z"/></svg>DEDICATED WINE SERVICE</div>
      <div class="perk"><svg viewBox="0 0 10 10"><path d="M5 0l1.5 3.3 3.5.4-2.6 2.4.7 3.5L5 7.8 1.9 9.6l.7-3.5L0 3.7l3.5-.4z"/></svg>BOTTLE OF WINE SOUVENIR</div>
      <div class="perk"><svg viewBox="0 0 10 10"><path d="M5 0l1.5 3.3 3.5.4-2.6 2.4.7 3.5L5 7.8 1.9 9.6l.7-3.5L0 3.7l3.5-.4z"/></svg>CUSTOM ART KEEPSAKE</div>
      <div class="perk"><svg viewBox="0 0 10 10"><path d="M5 0l1.5 3.3 3.5.4-2.6 2.4.7 3.5L5 7.8 1.9 9.6l.7-3.5L0 3.7l3.5-.4z"/></svg>PRIME TABLE PLACEMENT</div>
    </div>
    <div class="block details" style="top:388px;font-size:7.3px">
      <b>WHEN:</b>NOVEMBER 18TH, 2025<br>COCKTAILS 6:00PM | VIP TICKET HOLDERS 5:00PM<br>
      <b>WHERE:</b> PELICAN KEY - 4120 SEASIDE HWY<br>CORAL POINT<br>
      <b>DRESS:</b> COCKTAIL ATTIRE - <b>SPACE IS LIMITED</b></div>
    <div class="silver-rule" style="top:438px"></div>
    <div class="sea sea--foot" style="top:440px;height:37px" role="img" aria-label="Turquoise reef water"></div>
    <div class="block url" style="top:453px;font-size:7.6px;color:var(--white)">WWW.SAVEHARBORBEACON.ORG</div>
  </section>

</div>
</body>
</html>
```